Core Investment Strategy's Super Pie Chart

We need a one page visual explanation of an investment strategy we call "Core/Perimeter". This strategy emphasizes a "core" portfolio that will seldom change and "perimeter" investments that will change. Our investment management firm caters to wealthy individuals. We want to project an image of strength and reliability. At the same time, we are willing to explore new concepts. I have uploaded a PDF of my graphically-challenged assistant's attempt at creating the one page visual.

Industry/Entity Type

Investment

```html
<!DOCTYPE html>
<html lang="en">
<head>
<meta charset="utf-8">
<title>Core/Perimeter Portfolio</title>
<link rel="stylesheet" href="https://fonts.googleapis.com/css2?family=Libre+Baskerville:wght@400;700&family=EB+Garamond:wght@400;500&display=swap">
<style>
  :root {
    --page: #f5f5f5;
    --ink: #3a3a3a;
    --label: #555555;
    --leader: #9a9a9a;
    --white: #ffffff;
    --funds: #8e1a55;
    --funds-side: #6b0c3e;
    --alt: #5b2180;
    --alt-side: #431461;
    --core-assets: #d21a6d;
    --core-assets-side: #a80f52;
    --other: #262a7d;
    --other-side: #171a5c;
    --blue-light: #2cc8f4;
    --blue-deep: #0092d5;
    --green-light: #8dc63f;
    --green-deep: #2f8d3e;
  }
  html, body {
    margin: 0;
    padding: 0;
    width: 1200px;
    height: 1000px;
    overflow: hidden;
    background: var(--page);
  }
  .portfolio-sheet {
    position: relative;
    width: 1200px;
    height: 1000px;
    background: var(--page);
  }
  .sheet-title {
    position: absolute;
    top: 30px;
    left: 0;
    width: 1226px;
    margin: 0;
    text-align: center;
    font-family: "Libre Baskerville", Georgia, serif;
    font-weight: 700;
    font-size: 26px;
    color: var(--ink);
  }
  .chart {
    position: absolute;
    top: 0;
    left: 0;
  }
  .perimeter-label {
    font-family: "EB Garamond", Georgia, serif;
    font-size: 19px;
    fill: #222222;
  }
  .perimeter-value {
    font-family: "EB Garamond", Georgia, serif;
    font-size: 20px;
    fill: var(--white);
  }
  .slice-value {
    font-family: "Libre Baskerville", Georgia, serif;
    font-weight: 700;
    font-size: 19px;
    fill: var(--label);
  }
  .slice-name {
    font-family: "Libre Baskerville", Georgia, serif;
    font-weight: 700;
    font-size: 11.5px;
    fill: var(--label);
  }
  .leader {
    fill: none;
    stroke: var(--leader);
    stroke-width: 1.2;
  }
</style>
</head>
<body>
<main class="portfolio-sheet">
  <h1 class="sheet-title">Core/Perimeter Portfolio</h1>

  <svg class="chart" width="1200" height="1000" viewBox="0 0 1200 1000" role="img" aria-label="Core/Perimeter portfolio allocation chart">
    <defs>
      <linearGradient id="blue-fill" x1="0" y1="0" x2="1" y2="0.3">
        <stop offset="0" stop-color="var(--blue-light)"/>
        <stop offset="1" stop-color="var(--blue-deep)"/>
      </linearGradient>
      <linearGradient id="blue-fill-down" x1="0" y1="0" x2="0" y2="1">
        <stop offset="0" stop-color="var(--blue-light)"/>
        <stop offset="1" stop-color="var(--blue-deep)"/>
      </linearGradient>
      <linearGradient id="green-fill" x1="1" y1="0.3" x2="0" y2="0.6">
        <stop offset="0" stop-color="var(--green-light)"/>
        <stop offset="1" stop-color="var(--green-deep)"/>
      </linearGradient>
      <radialGradient id="pie-halo" cx="0.5" cy="0.5" r="0.5">
        <stop offset="0.55" stop-color="#d8d8d8" stop-opacity="0.9"/>
        <stop offset="1" stop-color="#f5f5f5" stop-opacity="0"/>
      </radialGradient>
      <filter id="slice-shadow" x="-20%" y="-20%" width="140%" height="140%">
        <feDropShadow dx="-2" dy="4" stdDeviation="5" flood-color="#000" flood-opacity="0.3"/>
      </filter>
    </defs>

    <!-- Perimeter bars -->
    <g class="perimeter-bars">
      <text class="perimeter-label" x="607" y="154" text-anchor="end">Actively Managed Mutual Funds</text>
      <path d="M838,168 L848,176 L836,206 L828,207 Z" fill="var(--funds-side)"/>
      <path d="M617,123 Q740,130 838,168 L828,207 Q730,172 620,168 Z" fill="var(--funds)"/>
      <text class="perimeter-value" x="626" y="153">8%</text>

      <text class="perimeter-label" x="607" y="200" text-anchor="end">Alternative Assets</text>
      <path d="M748,182 L756,190 L749,222 L740,224 Z" fill="var(--alt-side)"/>
      <path d="M620,170 Q690,172 748,182 L740,224 Q690,216 622,214 Z" fill="var(--alt)"/>
      <text class="perimeter-value" x="626" y="201">7%</text>

      <text class="perimeter-label" x="607" y="246" text-anchor="end">Attractive Core Assets</text>
      <path d="M693,226 L699,232 L696,260 L688,262 Z" fill="var(--core-assets-side)"/>
      <path d="M622,217 Q665,218 693,226 L688,262 Q660,258 624,260 Z" fill="var(--core-assets)"/>
      <text class="perimeter-value" x="626" y="246">3%</text>

      <text class="perimeter-label" x="607" y="296" text-anchor="end">Other</text>
      <path d="M668,272 L676,278 L674,311 L666,312 Z" fill="var(--other-side)"/>
      <path d="M625,266 Q650,266 668,272 L666,312 Q650,313 630,310 Z" fill="var(--other)"/>
      <text class="perimeter-value" x="628" y="295">2%</text>
    </g>

    <!-- Core pie -->
    <circle cx="635" cy="608" r="300" fill="url(#pie-halo)"/>
    <g class="core-pie" filter="url(#slice-shadow)">
      <path class="slice lg-cap" d="M635,608 L635,338 A270,270 0 0 1 900,660 Z" fill="url(#blue-fill)"/>
      <path class="slice mid-cap" d="M635,608 L773,642 A142,142 0 0 1 750,691 Z" fill="url(#blue-fill)"/>
      <path class="slice sm-cap" d="M635,608 L739,702 A140,140 0 0 1 683,740 Z" fill="url(#blue-fill)"/>
      <path class="slice intl-equities" d="M635,608 L664,816 A210,210 0 0 1 543,797 Z" fill="url(#blue-fill-down)"/>
      <path class="slice intermediate-bonds" d="M635,608 L464,785 A246,246 0 0 1 410,508 Z" fill="url(#green-fill)"/>
      <path class="slice short-bonds" d="M635,608 L480,482 A200,200 0 0 1 583,415 Z" fill="url(#green-fill)"/>
    </g>

    <!-- Leaders and labels -->
    <g class="pie-labels">
      <polyline class="leader" points="520,445 483,364 357,364"/>
      <text class="slice-value" x="428" y="358" text-anchor="middle">10%</text>
      <text class="slice-name" x="420" y="380" text-anchor="middle">Short-Term Bonds</text>

      <polyline class="leader" points="830,432 895,376 995,376"/>
      <text class="slice-value" x="938" y="368" text-anchor="middle">30%</text>
      <text class="slice-name" x="936" y="390" text-anchor="middle">Lg. Cap Equities</text>

      <polyline class="leader" points="397,578 317,632 180,632"/>
      <text class="slice-value" x="246" y="626" text-anchor="middle">20%</text>
      <text class="slice-name" x="181" y="648">Intermediate&#160; Bonds</text>

      <polyline class="leader" points="750,670 822,725 942,725"/>
      <text class="slice-value" x="880" y="720" text-anchor="middle">5%</text>
      <text class="slice-name" x="882" y="742" text-anchor="middle">Mid Cap Equities</text>

      <polyline class="leader" points="695,728 765,783 883,783"/>
      <text class="slice-value" x="828" y="778" text-anchor="middle">5%</text>
      <text class="slice-name" x="829" y="800" text-anchor="middle">Sm. Cap Equities</text>

      <polyline class="leader" points="613,808 655,884 787,884"/>
      <text class="slice-value" x="718" y="878" text-anchor="middle">10%</text>
      <text class="slice-name" x="724" y="900" text-anchor="middle">Int'l/Dev. Equities</text>
    </g>
  </svg>
</main>
</body>
</html>
```